Insurance Agency website design for Vell Harbor Insurance, LP

Build a website for Vell Harbor Insurance, LP which sells Homeowners, Auto, Renters, Condo, Flood, Disability, Life, Umbrella, and health insurance. We need the coolest insurance agency website out there to get quotes, contact us, or get additional information. Please list the following insurance companies we work with: Dranko, Pruvell, Corvane Mutual, Saldrie, Wendmarch, Kwelt, and Plumeworth.

Make a design similar to https://www.brimlockagents.example/

Selling personal insurance policies

```html
<!DOCTYPE html>
<html lang="en">
<head>
<meta charset="utf-8">
<title>Vell Harbor Insurance, LP</title>
<link href="https://fonts.googleapis.com/css2?family=Quicksand:wght@600;700&family=Montserrat:wght@400;500;600;700&display=swap" rel="stylesheet">
<style>
:root{
  --blue:#1a6fc0;
  --blue-deep:#0f5aa6;
  --blue-sky:#3b97e3;
  --navy:#12336e;
  --green:#6ab33c;
  --green-dark:#559a2a;
  --tint:#e9eff9;
  --tint-2:#eef3fa;
  --line:#c9d8ee;
  --text:#3b4660;
  --white:#ffffff;
}
*{box-sizing:border-box;margin:0;padding:0}
html,body{width:1200px;height:4274px;overflow:hidden}
body{position:relative;font-family:'Montserrat',sans-serif;color:var(--text);background:var(--white)}
.abs{position:absolute}
h1,h2,h3,.brand-name{font-family:'Quicksand',sans-serif;font-weight:700}
.btn{position:absolute;display:flex;align-items:center;justify-content:center;gap:8px;background:var(--green);color:var(--white);font-weight:700;font-size:13px;border-radius:26px;letter-spacing:.3px}
.eyebrow{position:absolute;font-size:13px;letter-spacing:2px;color:var(--green);font-weight:600}

.topbar{top:0;left:0;width:1200px;height:30px;background:#e4edf8}
.topbar a{position:absolute;top:8px;font-size:11px;color:var(--blue);font-weight:500}
.nav{top:30px;left:0;width:1200px;height:83px;background:var(--white)}
.brand{position:absolute;display:flex;align-items:center;gap:10px}
.brand-mark{width:38px;height:38px;border:3px solid var(--blue);border-radius:4px}
.brand-name{font-size:17px;line-height:19px;color:var(--blue)}
.nav-link{position:absolute;top:36px;font-size:13px;font-weight:600;color:var(--navy)}

.hero{top:113px;left:0;width:1200px;height:621px;background:linear-gradient(100deg,#1565ac 0%,#1f78c9 55%,#3a95e4 100%);overflow:hidden}
.hero-skyline{left:0;bottom:0;width:1200px;height:130px;background:linear-gradient(180deg,rgba(255,255,255,0) 0%,rgba(255,255,255,.08) 100%)}
.hero-badge{left:90px;top:95px;background:var(--green);color:var(--white);font-size:15px;letter-spacing:2px;font-weight:600;padding:6px 18px}
.hero h1{position:absolute;left:90px;top:130px;font-size:54px;line-height:53px;color:var(--white)}
.hero-copy{left:92px;top:254px;width:500px;font-size:16px;line-height:23px;color:var(--white)}
.hero-note{left:90px;top:412px;font-size:16px;color:var(--white);font-weight:500}
.hero-contact{top:458px;font-size:16px;color:var(--white);font-weight:600;display:flex;align-items:center;gap:10px}
.hero-photo{left:666px;top:94px;width:452px;height:425px;border-radius:40px 0 0 0;background:linear-gradient(160deg,#a9cdf0 0%,#6fa8dc 45%,#4a6f96 100%)}
.hero-stat{left:604px;top:250px;width:142px;height:142px;border-radius:50%;background:var(--white);border:6px solid #cfe2f6;display:flex;flex-direction:column;align-items:center;justify-content:center}
.hero-stat b{font-family:'Quicksand',sans-serif;font-size:34px;color:var(--blue)}
.hero-stat span{font-size:14px;color:var(--green);font-weight:700}

.carriers{top:734px;left:0;width:1200px;height:109px;background:var(--white);display:flex;align-items:center;justify-content:space-around;padding:0 90px}
.carrier{font-family:'Montserrat',sans-serif;font-weight:700;font-size:26px;color:#1d2a44}

.about{top:843px;left:0;width:1200px;height:664px;background:var(--white);overflow:hidden}
.about-photo{left:95px;top:87px;width:464px;height:464px;border-radius:50%;border:10px solid #dbe8f6;background:linear-gradient(170deg,#e7e3de 0%,#c9b39b 55%,#8f7462 100%)}
.tag{position:absolute;display:flex;align-items:center;gap:6px;font-size:14px;font-weight:700;border-radius:24px;padding:10px 18px}
.tag-light{background:var(--white);color:var(--navy);box-shadow:0 4px 12px rgba(15,50,110,.15)}
.tag-blue{background:var(--blue);color:var(--white)}
.about h2{position:absolute;left:638px;top:118px;font-size:40px;line-height:47px;color:var(--blue)}
.about h2 span{color:var(--navy)}
.about-copy{left:640px;top:225px;width:535px;font-size:16px;line-height:23px}
.about-copy p{margin-bottom:14px}

.coverage{top:1507px;left:0;width:1200px;height:659px;background:var(--tint);overflow:hidden}
.coverage h2{position:absolute;left:0;top:95px;width:1200px;text-align:center;font-size:32px;line-height:42px;color:var(--blue)}
.coverage h2 span{color:var(--navy)}
.coverage-note{left:0;top:200px;width:1200px;text-align:center;font-size:17px;color:#2b3550}
.cover-card{position:absolute;width:153px;height:128px;background:var(--white);border:1px solid var(--line);border-radius:6px;text-align:center}
.cover-card .check{position:absolute;left:12px;top:12px;width:18px;height:18px;border:1px solid var(--line);border-radius:3px;background:#f3f6fb}
.cover-card svg{position:absolute;left:50%;top:36px;transform:translateX(-50%)}
.cover-card span{position:absolute;left:0;bottom:18px;width:100%;font-size:14px;color:var(--blue);font-weight:500}

.agent-card{left:98px;top:2240px;width:989px;height:504px;background:var(--white);border:2px solid #cfe0f3;border-radius:4px}
.agent-deco-a{left:86px;top:2228px;width:160px;height:80px;background:#dce9f7}
.agent-deco-b{left:960px;top:2620px;width:140px;height:136px;background:#dce9f7}
.agent-photo{left:148px;top:2305px;width:400px;height:400px;border-radius:50%;background:linear-gradient(160deg,#2f86d7 0%,#1a67b4 100%)}
.agent h2{position:absolute;left:632px;top:2296px;font-size:36px;line-height:35px;color:var(--blue)}
.agent h2 span{color:var(--navy)}
.agent-sub{left:632px;top:2384px;width:410px;font-size:13px;line-height:19px;color:var(--blue);font-weight:500}
.field-label{position:absolute;font-size:14px;color:#2b3550}
.field{position:absolute;height:48px;border:1px solid #a9c4e6;border-radius:3px;display:flex;align-items:center;gap:10px;padding-left:16px;font-size:13px;color:#6c7890;background:var(--white)}

.testimonials{top:2822px;left:0;width:1200px;height:489px;background:var(--tint-2);overflow:hidden}
.testimonials h2{position:absolute;left:106px;top:150px;font-size:34px;line-height:36px;color:var(--blue)}
.testimonials h2 span{color:var(--navy)}
.arrow-btn{position:absolute;width:40px;height:40px;border-radius:50%;background:var(--white);display:flex;align-items:center;justify-content:center;box-shadow:0 3px 10px rgba(15,50,110,.12)}
.review{position:absolute;top:93px;width:322px;height:262px;background:var(--white);border:1px solid #d9e3f1;border-radius:4px;padding:28px 30px}
.review q{display:block;margin-top:22px;font-size:13px;line-height:22px;font-style:italic;color:#2b3550;quotes:none}
.review .quote-mark{font-family:'Quicksand',sans-serif;font-size:50px;line-height:30px;color:#b7d0ee;font-weight:700}
.reviewer{position:absolute;left:24px;bottom:26px;display:flex;align-items:center;gap:10px;font-size:12px;font-weight:600;color:#2b3550}
.avatar{width:36px;height:36px;border-radius:50%;background:#c9b7a6}
.stars{color:#f5b400;font-size:15px;letter-spacing:6px}
.source-dot{position:absolute;right:24px;bottom:30px;width:22px;height:22px;border-radius:50%;background:#d7e2f1}

.contact{top:3311px;left:0;width:1200px;height:548px;background:#1b6db5;overflow:hidden}
.contact h2{position:absolute;left:124px;top:125px;font-size:36px;color:var(--white)}
.contact-copy{left:126px;top:190px;width:470px;font-size:15px;line-height:19px;color:var(--white)}
.contact-copy p{margin-bottom:10px}
.contact .field{border-color:rgba(255,255,255,.7);background:transparent;color:var(--white);width:450px;font-size:14px}

.footer{top:3859px;left:0;width:1200px;height:415px;background:#0e5aa5;color:var(--white)}
.footer .brand-name{color:var(--white)}
.footer .brand-mark{border-color:var(--white)}
.footer-col h3{font-family:'Montserrat',sans-serif;font-size:15px;font-weight:700;border-left:3px solid var(--green);padding-left:12px;margin-bottom:16px}
.footer-col li{list-style:none;font-size:12px;line-height:26px;padding-left:15px}
.social{position:absolute;width:24px;height:24px;border-radius:50%;background:rgba(255,255,255,.9)}
.footer-bottom{left:0;top:316px;width:1200px;border-top:1px solid rgba(255,255,255,.2)}
.dash{position:absolute;border:0 dashed #3b8ad6}
</style>
</head>
<body>

<div class="abs topbar">
  <a style="left:889px">Contact Us</a>
  <a style="left:984px">Sign Up</a>
  <a style="left:1067px">Log In</a>
</div>

<header class="abs nav">
  <div class="brand" style="left:110px;top:20px">
    <div class="brand-mark"></div>
    <div class="brand-name">VELL HARBOR<br><span style="color:var(--navy);font-weight:600">INSURANCE, LP</span></div>
  </div>
  <span class="nav-link" style="left:384px">GET INSURANCE ▾</span>
  <span class="nav-link" style="left:542px">PERSONAL ▾</span>
  <span class="nav-link" style="left:668px">WHY US</span>
  <span class="nav-link" style="left:770px;top:33px;font-size:16px;display:flex;gap:8px;align-items:center">
    <svg width="16" height="16" viewBox="0 0 24 24"><path fill="#6ab33c" d="M6.6 10.8a15 15 0 006.6 6.6l2.2-2.2a1 1 0 011-.25 11 11 0 003.6.6 1 1 0 011 1V20a1 1 0 01-1 1A17 17 0 013 4a1 1 0 011-1h3.5a1 1 0 011 1 11 11 0 00.6 3.6 1 1 0 01-.25 1z"/></svg>(555) 014-0486</span>
  <div class="btn" style="left:946px;top:22px;width:141px;height:40px;font-size:12px">GET A QUOTE ›</div>
</header>

<section class="abs hero">
  <div class="abs hero-skyline" role="img" aria-label="Faint city skyline outline"></div>
  <div class="abs hero-badge">VELL HARBOR INSURANCE LP</div>
  <h1>Protecting What<br>Matters Most</h1>
  <p class="abs hero-copy">At Vell Harbor Insurance, we understand that your peace of mind is invaluable. Our mission is to protect what matters most to you—your home, your vehicle, your health, and your loved ones. With our comprehensive range of insurance solutions, we are dedicated to safeguarding your assets and providing you with the security you deserve.</p>
  <p class="abs hero-note">For inquiries, please contact us at</p>
  <div class="abs hero-contact" style="left:90px">
    <svg width="20" height="20" viewBox="0 0 24 24"><path fill="#fff" d="M6.6 10.8a15 15 0 006.6 6.6l2.2-2.2a1 1 0 011-.25 11 11 0 003.6.6 1 1 0 011 1V20a1 1 0 01-1 1A17 17 0 013 4a1 1 0 011-1h3.5a1 1 0 011 1 11 11 0 00.6 3.6 1 1 0 01-.25 1z"/></svg>(555) 014-0486</div>
  <div class="abs hero-contact" style="left:276px">
    <svg width="20" height="16" viewBox="0 0 24 18"><rect x="1" y="1" width="22" height="16" rx="2" fill="#fff"/><path d="M2 2l10 8 10-8" stroke="#1a6fc0" stroke-width="2" fill="none"/></svg>info@VellHarborInsurance.example</div>
  <div class="abs hero-photo" role="img" aria-label="Photo of a smiling couple embracing outdoors"></div>
  <div class="abs hero-stat"><b>20+</b><span>PRODUCTS</span></div>
</section>

<section class="abs carriers" aria-label="Partner carriers">
  <span class="carrier" style="letter-spacing:5px;font-size:22px">DRANKO</span>
  <span class="carrier" style="letter-spacing:5px">PRUVELL</span>
  <span class="carrier" style="color:#f07a12">Corvane Mutual</span>
  <span class="carrier" style="color:#1e3a6e">Saldrie</span>
  <span class="carrier" style="color:#d0202a">Kwelt</span>
</section>

<section class="abs about">
  <svg class="abs" style="left:0;top:0" width="430" height="664" role="img" aria-label="Green band over a house photo">
    <polygon points="0,0 428,0 190,664 0,664" fill="#7bbd4a"/>
  </svg>
  <div class="abs about-photo" role="img" aria-label="Photo of a family sitting together making a roof shape with their arms"></div>
  <div class="tag tag-light" style="left:75px;top:320px">⌂ Protect Home</div>
  <div class="tag tag-blue" style="left:450px;top:293px">♡ Your Health</div>
  <div class="tag tag-light" style="left:358px;top:478px">Protect Vehicle</div>
  <span class="eyebrow" style="left:638px;top:100px">WHO WE ARE</span>
  <h2>About Vell Harbor<br><span>Insurance, LP</span></h2>
  <div class="dash" style="left:1010px;top:189px;width:190px;border-top-width:2px"></div>
  <div class="abs about-copy">
    <p>Vell Harbor Insurance is a full-service, independent insurance agency with over three decades of experience in delivering comprehensive insurance solutions to individuals.</p>
    <p>We proudly offer a diverse portfolio of products from more than 20 of the most reputable and financially secure companies in the industry. Our dedicated team of over 50 skilled professionals is committed to customizing these products and services to meet the unique needs of each client.</p>
    <p>At Vell Harbor Insurance, our experts are focused on addressing the individual needs of our clients, ensuring exceptional service and support at every step</p>
  </div>
  <div class="btn" style="left:636px;top:525px;width:173px;height:50px">GET A QUOTE ›</div>
  <div class="dash" style="left:610px;top:620px;width:108px;height:44px;border-top-width:2px;border-left-width:2px"></div>
  <div class="dash" style="left:717px;top:575px;height:45px;border-left-width:2px"></div>
</section>

<section class="abs coverage">
  <div class="dash" style="left:610px;top:0;height:60px;border-left-width:2px"></div>
  <span class="eyebrow" style="left:0;top:72px;width:1200px;text-align:center">GET STARTED NOW</span>
  <h2>Now more Specifically, what type of<br><span>Personal Protection are you looking for?</span></h2>
  <p class="abs coverage-note">Select up to three coverages</p>

  <div class="cover-card" style="left:255px;top:243px"><div class="check"></div>
    <svg width="70" height="40" viewBox="0 0 70 40" fill="none" stroke="#1a6fc0" stroke-width="2.5"><path d="M4 26h62v-8l-10-2-8-8H22l-8 8-10 2z"/><circle cx="18" cy="28" r="5"/><circle cx="52" cy="28" r="5"/></svg>
    <span>Auto</span></div>
  <div class="cover-card" style="left:440px;top:243px"><div class="check"></div>
    <svg width="46" height="44" viewBox="0 0 46 44" fill="none" stroke="#1a6fc0" stroke-width="2.5"><path d="M4 20L23 4l19 16M8 17v24h30V17"/><rect x="18" y="26" width="10" height="15"/></svg>
    <span>Home</span></div>
  <div class="cover-card" style="left:625px;top:243px"><div class="check"></div>
    <svg width="46" height="46" viewBox="0 0 46 46" fill="none" stroke="#1a6fc0" stroke-width="2.5"><circle cx="30" cy="14" r="9"/><path d="M24 20L6 38l4 4 3-3 3 3 4-4-3-3 8-8"/></svg>
    <span>Renters</span></div>
  <div class="cover-card" style="left:810px;top:243px"><div class="check"></div>
    <svg width="46" height="46" viewBox="0 0 46 46" fill="none" stroke="#1a6fc0" stroke-width="2.5"><rect x="8" y="6" width="30" height="36"/><path d="M14 14h4M22 14h4M30 14h2M14 22h4M22 22h4M30 22h2M14 30h4M30 30h2M20 42v-8h6v8"/></svg>
    <span>Condo</span></div>
  <div class="cover-card" style="left:255px;top:393px"><div class="check"></div>
    <svg width="50" height="46" viewBox="0 0 50 46" fill="none" stroke="#1a6fc0" stroke-width="2.5"><path d="M4 18a21 14 0 0142 0zM25 4v14"/><circle cx="14" cy="28" r="4"/><circle cx="25" cy="28" r="4"/><circle cx="36" cy="28" r="4"/><path d="M7 42a7 7 0 0114 0M18 42a7 7 0 0114 0M29 42a7 7 0 0114 0"/></svg>
    <span>Umbrella</span></div>
  <div class="cover-card" style="left:440px;top:393px"><div class="check"></div>
    <svg width="56" height="40" viewBox="0 0 56 40" fill="none" stroke="#1a6fc0" stroke-width="2.5"><path d="M4 10l48-6v30H4z"/><rect x="12" y="16" width="10" height="18"/><rect x="28" y="16" width="16" height="10"/></svg>
    <span>Mobile Home</span></div>
  <div class="cover-card" style="left:625px;top:393px"><div class="check"></div>
    <svg width="62" height="40" viewBox="0 0 62 40" fill="none" stroke="#1a6fc0" stroke-width="2.5"><path d="M4 6h40v8h10l4 10v8H4z"/><rect x="10" y="12" width="10" height="8"/><circle cx="16" cy="33" r="4"/><circle cx="46" cy="33" r="4"/></svg>
    <span>Motor Home</span></div>
  <div class="cover-card" style="left:810px;top:393px"><div class="check"></div>
    <svg width="62" height="40" viewBox="0 0 62 40" fill="none" stroke="#1a6fc0" stroke-width="2.5"><circle cx="12" cy="28" r="8"/><circle cx="50" cy="28" r="8"/><path d="M12 28l10-12h16l12 12M26 16l4-8h8"/></svg>
    <span>ATV</span></div>

  <div class="btn" style="left:518px;top:556px;width:173px;height:50px">SHOW MORE ›</div>
</section>

<section class="agent">
  <div class="abs agent-deco-a"></div>
  <div class="abs agent-deco-b"></div>
  <div class="abs agent-card"></div>
  <div class="abs agent-photo" role="img" aria-label="Photo of a smiling woman holding an open laptop"></div>
  <h2>Find &nbsp;the right local<br><span>Agent for you</span></h2>
  <p class="abs agent-sub">Just some basic information. The address of your personal property will help in finding the right local agent for you.</p>
  <span class="field-label" style="left:638px;top:2450px">Enter the address of your insurable property</span>
  <div class="field" style="left:635px;top:2481px;width:386px">
    <svg width="16" height="12" viewBox="0 0 24 18"><rect x="1" y="1" width="22" height="16" rx="2" fill="#9bb3d4"/></svg>Email address</div>
  <span class="field-label" style="left:638px;top:2550px">Zip code (require)</span>
  <div class="field" style="left:637px;top:2576px;width:386px">
    <svg width="12" height="16" viewBox="0 0 12 16"><path d="M6 0a6 6 0 016 6c0 4-6 10-6 10S0 10 0 6a6 6 0 016-6z" fill="#9bb3d4"/></svg>Type Zip code</div>
  <div class="btn" style="left:631px;top:2646px;width:173px;height:46px;font-size:14px">NEXT STEP ›</div>
  <svg class="abs" style="left:500px;top:2600px" width="120" height="110" fill="none"><path d="M6 4c10 80 70 100 106 70" stroke="#3b8ad6" stroke-width="2" stroke-dasharray="4 4"/><path d="M106 66l8 6-10 4z" fill="#1a6fc0"/></svg>
  <div class="dash" style="left:218px;top:2768px;width:110px;height:54px;border-bottom-width:2px;border-right-width:2px"></div>
</section>

<section class="abs testimonials">
  <div class="dash" style="left:218px;top:0;height:90px;border-left-width:2px"></div>
  <span class="eyebrow" style="left:106px;top:130px">TESTIMONIALS</span>
  <h2>What Our Client<br><span>Says about us</span></h2>
  <p class="abs" style="left:106px;top:235px;width:280px;font-size:13px;line-height:20px">Lorem ipsum dolor sit amet, consectetur adipiscing elit, sed do eiusmod</p>
  <div class="arrow-btn" style="left:106px;top:294px"><svg width="16" height="14"><path d="M15 7H2M7 2L2 7l5 5" stroke="#1a6fc0" stroke-width="2" fill="none"/></svg></div>
  <div class="arrow-btn" style="left:158px;top:294px"><svg width="16" height="14"><path d="M1 7h13M9 2l5 5-5 5" stroke="#1a6fc0" stroke-width="2" fill="none"/></svg></div>

  <article class="review" style="left:430px">
    <div class="quote-mark">“</div>
    <q>“Lorem ipsum dolor sit amet, consecte-tur adipiscing elit, sed do eiusmod tempor incididunt ut labore et dolore magna aliqua. Ut enim ad minim veniam, quis nostrud exercitation”</q>
    <div class="reviewer"><div class="avatar" role="img" aria-label="Reviewer portrait"></div><div>Marla Fenn<div class="stars">★★★★★</div></div></div>
    <div class="source-dot"></div>
  </article>
  <article class="review" style="left:768px">
    <div class="quote-mark">“</div>
    <q>“Lorem ipsum dolor sit amet, consecte-tur adipiscing elit, sed do eiusmod tempor incididunt ut labore et dolore magna aliqua. Ut enim ad minim veniam, quis nostrud exercitation”</q>
    <div class="reviewer"><div class="avatar" role="img" aria-label="Reviewer portrait"></div><div>Marla Fenn<div class="stars">★★★★★</div></div></div>
    <div class="source-dot"></div>
  </article>
  <article class="review" style="left:1106px">
    <div class="quote-mark">“</div>
    <q>“Lorem ipsum dolor sit amet, consecte-tur adipiscing elit, sed do eiusmod tempor incididunt ut labore et dolore magna aliqua. Ut enim ad minim veniam, quis nostrud exercitation”</q>
    <div class="reviewer"><div class="avatar" role="img" aria-label="Reviewer portrait"></div><div>Marla Fenn<div class="stars">★★★★★</div></div></div>
  </article>
</section>

<section class="abs contact">
  <div class="dash" style="left:0;top:48px;width:64px;height:84px;border-top-width:2px;border-right-width:2px;border-color:#6aaef0"></div>
  <div class="dash" style="left:64px;top:132px;width:48px;border-top-width:2px;border-color:#6aaef0"></div>
  <span class="eyebrow" style="left:124px;top:105px;color:var(--white)">CONTACT US</span>
  <h2>Get a Quote</h2>
  <div class="abs contact-copy">
    <p>We believe that securing your home is one of the most important decisions you can make. Obtaining a comprehensive insurance quote is essential to understanding your coverage options and ensuring that your property is adequately protected against unforeseen events.</p>
    <p>Our team of experienced professionals is here to guide you through the process, helping you find the right policy that meets your specific needs and budget. Don't leave your home's safety to chance—get a quote today and take the first step towards peace of mind.</p>
  </div>
  <div class="field" style="left:648px;top:96px">
    <svg width="14" height="16" viewBox="0 0 14 16"><circle cx="7" cy="4.5" r="4" fill="#fff"/><path d="M0 16a7 6 0 0114 0z" fill="#fff"/></svg>First Name</div>
  <div class="field" style="left:648px;top:154px">
    <svg width="14" height="16" viewBox="0 0 14 16"><circle cx="7" cy="4.5" r="4" fill="#fff"/><path d="M0 16a7 6 0 0114 0z" fill="#fff"/></svg>Last Name</div>
  <div class="field" style="left:648px;top:212px">
    <svg width="16" height="12" viewBox="0 0 24 18"><rect x="1" y="1" width="22" height="16" rx="2" fill="#fff"/></svg>Email address</div>
  <div class="field" style="left:648px;top:270px">
    <svg width="16" height="16" viewBox="0 0 24 24"><path fill="#fff" d="M6.6 10.8a15 15 0 006.6 6.6l2.2-2.2a1 1 0 011-.25 11 11 0 003.6.6 1 1 0 011 1V20a1 1 0 01-1 1A17 17 0 013 4a1 1 0 011-1h3.5a1 1 0 011 1 11 11 0 00.6 3.6 1 1 0 01-.25 1z"/></svg>Phone</div>
  <div class="field" style="left:648px;top:328px;height:88px;align-items:flex-start;padding-top:16px">
    <svg width="16" height="14" viewBox="0 0 16 14"><ellipse cx="8" cy="6" rx="8" ry="6" fill="#fff"/></svg>Message</div>
  <div class="btn" style="left:647px;top:434px;width:202px;height:48px;font-size:15px">SEND MESSAGE ›</div>
</section>

<footer class="abs footer">
  <div class="brand" style="left:140px;top:70px">
    <div class="brand-mark"></div>
    <div class="brand-name">VELL HARBOR<br><span style="font-weight:600">INSURANCE, LP</span></div>
  </div>
  <p class="abs" style="left:140px;top:140px;width:230px;font-size:10px;line-height:14px">Lorem ipsum dolor sit amet, consectetur adipiscing elit, sed do eiusmod tempor incididunt ut labore et dolore</p>
  <div class="social" style="left:143px;top:206px" role="img" aria-label="Social profile"></div>
  <div class="social" style="left:192px;top:206px" role="img" aria-label="Social profile"></div>
  <div class="social" style="left:240px;top:206px" role="img" aria-label="Social profile"></div>

  <div class="abs footer-col" style="left:420px;top:76px"><h3>NAVIGATION</h3>
    <ul><li>Home</li><li>About Us</li><li>Insurance</li><li>Services</li><li>Testimonials</li></ul></div>
  <div class="abs footer-col" style="left:635px;top:76px"><h3>INSURANCE</h3>
    <ul><li>Auto Insurance</li><li>Home Insurance</li><li>Life Insurance</li><li>Car Insurance</li><li>Business Insurance</li></ul></div>
  <div class="abs footer-col" style="left:860px;top:76px"><h3>CONTACT US</h3>
    <div style="display:flex;gap:14px;font-size:12px;line-height:20px;padding-left:15px">
      <svg width="14" height="14" viewBox="0 0 24 24" style="margin-top:4px"><path fill="#fff" d="M6.6 10.8a15 15 0 006.6 6.6l2.2-2.2a1 1 0 011-.25 11 11 0 003.6.6 1 1 0 011 1V20a1 1 0 01-1 1A17 17 0 013 4a1 1 0 011-1h3.5a1 1 0 011 1 11 11 0 00.6 3.6 1 1 0 01-.25 1z"/></svg>
      <div>Phone Number<br>(555) 014-0486</div></div>
    <div style="display:flex;gap:14px;font-size:12px;line-height:20px;padding-left:15px;margin-top:18px">
      <svg width="14" height="12" viewBox="0 0 24 18" style="margin-top:5px"><rect x="1" y="1" width="22" height="16" rx="2" fill="#fff"/></svg>
      <div>Email address<br>info@VellHarborInsurance.example</div></div>
  </div>

  <div class="abs footer-bottom"></div>
  <p class="abs" style="left:137px;top:350px;font-size:10px">© 2025 Vell Harbor Insurance, LP. All Rights Reserved</p>
  <p class="abs" style="left:907px;top:344px;font-size:10px;word-spacing:2px">Terms of use &nbsp;Privacy Policy &nbsp;Sitemap</p>
</footer>

</body>
</html>
```